Bref créative
Modern Business Card for Computer Service Company
Brightwave Tech Partners, Inc.
Professional
Marcus T. Hollings
Technology Engineer
4195 Larkin Avenue
Hollywood FL 33024
marcus@btp-helpdesk.com
www.btp-helpdesk.com
I would like a blurb that says "Supporting South Florida Small Business"

```html
<!DOCTYPE html>
<html lang="en">
<head>
<meta charset="utf-8">
<title>Brightwave Tech Partners – Business Card</title>
<link rel="stylesheet" href="https://fonts.googleapis.com/css2?family=Exo+2:wght@400;600;800&display=swap">
<style>
  :root {
    --bg: #e4e6e8;
    --card: #ffffff;
    --green: #7cc23a;
    --green-dark: #4f9a1e;
    --blue: #1c6fb8;
    --ink: #2b2f33;
    --muted: #6b7177;
    --rule: #d9dde0;
  }
  * { box-sizing: border-box; margin: 0; padding: 0; }
  html, body { width: 1200px; height: 961px; overflow: hidden; }
  body {
    background: var(--bg);
    font-family: "Exo 2", Arial, sans-serif;
    color: var(--ink);
    position: relative;
  }
  .business-card {
    position: absolute;
    left: 170px; top: 235px;
    width: 860px; height: 490px;
    background: var(--card);
    box-shadow: 0 18px 40px rgba(0,0,0,.18);
    overflow: hidden;
  }
  .card-band { position: absolute; left: 0; top: 0; width: 860px; height: 110px; }
  .card-footer-line {
    position: absolute; left: 0; bottom: 0; width: 100%; height: 12px;
    background: linear-gradient(90deg, var(--green) 0 60%, var(--blue) 60% 100%);
  }
  .brand-block {
    position: absolute; left: 60px; top: 200px; width: 350px;
  }
  .brand {
    display: flex; align-items: center; gap: 16px;
  }
  .brand-mark { width: 46px; height: 46px; background: var(--blue); flex: none; }
  .brand-name {
    font-weight: 800; font-size: 30px; line-height: 1.1;
    color: var(--blue); letter-spacing: .5px; width: 260px;
  }
  .brand-tagline {
    margin-top: 22px; padding-top: 14px;
    border-top: 2px solid var(--green);
    font-size: 15px; font-weight: 600; line-height: 1.35;
    color: var(--green-dark);
    width: 320px;
  }
  .divider {
    position: absolute; left: 440px; top: 170px;
    width: 2px; height: 220px; background: var(--rule);
  }
  .contact { position: absolute; left: 480px; top: 170px; width: 350px; }
  .contact-name { font-size: 30px; font-weight: 600; color: var(--ink); line-height: 1.2; }
  .contact-title { font-size: 17px; color: var(--green-dark); margin: 4px 0 26px; }
  .contact-list { list-style: none; }
  .contact-list li {
    display: flex; align-items: center; gap: 12px;
    font-size: 16px; color: var(--muted); margin-bottom: 11px;
    white-space: nowrap;
  }
  .contact-list svg { width: 16px; height: 16px; flex: none; }
</style>
</head>
<body>
  <article class="business-card">
    <svg class="card-band" viewBox="0 0 860 110" aria-hidden="true">
      <polygon points="0,0 860,0 860,70 0,92" fill="var(--green)"/>
      <polygon points="0,92 860,70 860,82 0,104" fill="var(--blue)"/>
    </svg>

    <div class="brand-block">
      <div class="brand">
        <span class="brand-mark"></span>
        <span class="brand-name">Brightwave Tech Partners</span>
      </div>
      <p class="brand-tagline">Supporting South Florida Small Business</p>
    </div>

    <div class="divider"></div>

    <section class="contact">
      <h1 class="contact-name">Marcus T. Hollings</h1>
      <p class="contact-title">Technology Engineer</p>
      <ul class="contact-list">
        <li>
          <svg viewBox="0 0 16 16"><path d="M8 1a5 5 0 0 0-5 5c0 4 5 9 5 9s5-5 5-9a5 5 0 0 0-5-5zm0 7a2 2 0 1 1 0-4 2 2 0 0 1 0 4z" fill="var(--green-dark)"/></svg>
          4195 Larkin Avenue, Hollywood FL 33024
        </li>
        <li>
          <svg viewBox="0 0 16 16"><path d="M4 1l3 3-2 2a9 9 0 0 0 5 5l2-2 3 3-2 3C7 15 1 9 1 3z" fill="var(--green-dark)"/></svg>
          Tel: 954.555.0142
        </li>
        <li>
          <svg viewBox="0 0 16 16"><rect x="2" y="5" width="12" height="8" fill="var(--green-dark)"/><rect x="4" y="2" width="8" height="4" fill="var(--green-dark)"/></svg>
          Fax: 954.555.0143
        </li>
        <li>
          <svg viewBox="0 0 16 16"><rect x="1" y="3" width="14" height="10" fill="var(--green-dark)"/><path d="M1 3l7 6 7-6" stroke="#fff" fill="none"/></svg>
          marcus@btp-helpdesk.com
        </li>
        <li>
          <svg viewBox="0 0 16 16"><circle cx="8" cy="8" r="6.5" stroke="var(--green-dark)" stroke-width="1.5" fill="none"/><path d="M1.5 8h13M8 1.5c-3 3.5-3 9.5 0 13M8 1.5c3 3.5 3 9.5 0 13" stroke="var(--green-dark)" fill="none"/></svg>
          www.btp-helpdesk.com
        </li>
      </ul>
    </section>

    <div class="card-footer-line"></div>
  </article>
</body>
</html>
```